Digital Marketing Consultant Needs a Business Card Design

I need a business card to brand myself - I'm a digital marketing consultant, and I do web design, SEO, lead generation, social media, etc. I'm overhauling my website (CorinneDalworth.com) and just had a snazzy new logo made.

I like the combo of yellow & gray - I find it eye-catching, upbeat and techie. The exact colors of yellow and gray that I like are #F6BF27 and #6D6D6D. But I'm open to suggestions and other color combinations!

I plan on printing the card using some high-end printing techniques that will ensure the card stands out - either really thick cards with colored edges, or spot UV. Not sure which yet, so if you want to incorporate that into your design, that'd be great!

I'm looking for a clean and modern design, but something that will really stand out when paired with 'fancy' printing.

Target Market(s)

Small and medium-sized business owners.

Industry/Entity Type

Printing

Contact Information for Business Card

Corinne Dalworth
Digital Marketing
Call or Text: 850-555-0276
Corinne@CorinneDalworth.com
www.CorinneDalworth.com
@QRV58 on Twitter

Font styles to use
Serif
Sans Serif

Requirements
Must have
• My logo, my contact information, and my "company colors" - #F6BF27 and #6D6D6D.
Nice to have
• If there's room to mention all the things that I do:
• Social Media, Web Design, SEO, Lead Generation, Conversion Funnels, PPC
• (don't add if it makes the card cluttered)

```html
<!DOCTYPE html>
<html lang="en">
<head>
<meta charset="utf-8">
<title>Corinne Dalworth – Business Card</title>
<link rel="stylesheet" href="https://fonts.googleapis.com/css2?family=Marcellus&family=Arimo:wght@400;700&display=swap">
<style>
  :root {
    --brand-yellow: #F6BF27;
    --brand-gray: #6D6D6D;
    --gray-dark: #5e5e5e;
    --gray-light: #a9a9a9;
    --card-white: #ffffff;
    --card-off-white: #ececec;
    --backdrop: #e4e1dc;
    --text-gray: #555555;
  }
  * { box-sizing: border-box; margin: 0; padding: 0; }
  html, body { width: 1200px; height: 885px; overflow: hidden; }
  body {
    background: var(--backdrop);
    font-family: "Arimo", Arial, sans-serif;
    position: relative;
  }

  /* ---------- Front of card ---------- */
  .card-front {
    position: absolute;
    left: 50px; top: 150px;
    width: 640px; height: 366px;
    background: linear-gradient(150deg, #8a8a8a 0%, var(--gray-light) 45%, #7c7c7c 75%, var(--gray-dark) 100%);
    box-shadow: 0 10px 24px rgba(0,0,0,.25);
    color: var(--card-white);
  }
  .front-logo {
    position: absolute;
    left: 0; right: 0; top: 92px;
    display: flex; align-items: center; justify-content: center; gap: 16px;
  }
  .front-logo .mark {
    width: 40px; height: 40px;
    border: 2px solid var(--card-white);
  }
  .front-logo .wordmark {
    font-family: "Marcellus", Georgia, serif;
    font-size: 38px; letter-spacing: 3px;
  }
  .front-tagline {
    position: absolute; left: 0; right: 0; top: 150px;
    text-align: center;
    font-size: 12px; letter-spacing: 5px; text-transform: lowercase;
    opacity: .9;
  }
  .front-rule {
    position: absolute; left: 120px; right: 120px; top: 200px;
    height: 1px; background: rgba(255,255,255,.7);
  }
  .front-url {
    position: absolute; left: 0; right: 0; top: 222px;
    text-align: center; font-size: 17px; letter-spacing: .5px;
  }

  /* ---------- Back of card ---------- */
  .card-back {
    position: absolute;
    left: 770px; top: 110px;
    width: 380px; height: 665px;
    background: linear-gradient(160deg, var(--card-white) 0%, var(--card-off-white) 100%);
    box-shadow: 0 10px 24px rgba(0,0,0,.25);
    overflow: hidden;
  }
  .back-logo {
    position: absolute; left: 30px; top: 70px;
    display: flex; align-items: center; gap: 12px;
  }
  .back-logo .mark {
    width: 30px; height: 30px;
    border: 2px solid var(--brand-gray);
  }
  .back-logo .wordmark {
    font-family: "Marcellus", Georgia, serif;
    font-size: 27px; letter-spacing: 1.5px; color: var(--brand-gray);
  }
  .back-tagline {
    position: absolute; right: 30px; top: 112px;
    font-size: 9px; letter-spacing: 4px; color: var(--brand-gray);
  }
  .back-rule {
    position: absolute; left: 30px; width: 200px; top: 140px;
    height: 1px; background: var(--gray-light);
  }
  .services {
    position: absolute; left: 30px; right: 30px; top: 210px;
    font-size: 17px; line-height: 1.2; color: var(--text-gray);
  }
  .person {
    position: absolute; left: 30px; top: 320px;
  }
  .person .name {
    font-size: 27px; font-weight: 700; color: var(--brand-yellow);
  }
  .person .role {
    font-size: 19px; font-weight: 700; color: var(--text-gray); margin-top: 2px;
  }
  .contacts {
    position: absolute; left: 30px; top: 420px; list-style: none;
    font-size: 16px; color: var(--text-gray);
  }
  .contacts li { display: flex; align-items: center; gap: 12px; margin-bottom: 12px; }
  .contacts svg { width: 20px; height: 20px; flex: none; }
  .phone-band {
    position: absolute; left: 0; right: 0; bottom: 0; height: 90px;
    background: var(--brand-gray);
    display: flex; align-items: center; justify-content: center;
    font-size: 22px; color: var(--card-white); letter-spacing: .5px;
  }
</style>
</head>
<body>

<section class="card-front" aria-label="Business card front">
  <div class="front-logo">
    <span class="mark"></span>
    <span class="wordmark">CORINNE DALWORTH</span>
  </div>
  <p class="front-tagline">digital marketing</p>
  <div class="front-rule"></div>
  <p class="front-url">www.CorinneDalworth.com</p>
</section>

<section class="card-back" aria-label="Business card back">
  <div class="back-logo">
    <span class="mark"></span>
    <span class="wordmark">CORINNE DALWORTH</span>
  </div>
  <p class="back-tagline">digital marketing</p>
  <div class="back-rule"></div>

  <p class="services">Social Media, Web Design, SEO,<br>Lead Generation<br>Conversion Funnels, PPC</p>

  <div class="person">
    <p class="name">Corinne Dalworth</p>
    <p class="role">Digital Marketing</p>
  </div>

  <ul class="contacts">
    <li>
      <svg viewBox="0 0 20 20" aria-hidden="true"><rect width="20" height="20" fill="#F6BF27"/></svg>
      @QRV58 on Twitter
    </li>
    <li>
      <svg viewBox="0 0 20 20" aria-hidden="true">
        <rect width="20" height="20" fill="#F6BF27"/>
        <circle cx="10" cy="10" r="6" fill="none" stroke="#fff" stroke-width="1.5"/>
        <ellipse cx="10" cy="10" rx="2.6" ry="6" fill="none" stroke="#fff" stroke-width="1.2"/>
        <line x1="4" y1="10" x2="16" y2="10" stroke="#fff" stroke-width="1.2"/>
      </svg>
      www.CorinneDalworth.com
    </li>
    <li>
      <svg viewBox="0 0 20 20" aria-hidden="true">
        <rect width="20" height="20" fill="#F6BF27"/>
        <rect x="4" y="6" width="12" height="8" fill="none" stroke="#fff" stroke-width="1.4"/>
        <polyline points="4,6 10,11 16,6" fill="none" stroke="#fff" stroke-width="1.4"/>
      </svg>
      Corinne@CorinneDalworth.com
    </li>
  </ul>

  <div class="phone-band">Call or Text: 850-555-0276</div>
</section>

</body>
</html>
```